Photographer website, needs Pageboard design. (updated details in brief.)

Company name Tobin Vesky Photography, looking to add a Pageboard design, that is minimalistic, yet powerful. Less is more in my opinion, but what's there is creative, but eye catchy. see example image in files section for a better idea of what I am looking for. I have also added some source files for my logo.

Target Market(s)

local musicians/artists, models/fashion, and business professional looking for headshots or corporate business profile images.

Colors
0655a3
cfdfed
ffffff

Requirements
Must have
• I have added a screen shot of what I am looking for, for everyone to gain a better sense of my vision. Please see the uploaded files below.
Nice to have
• I am really a fan of the example image in the files section below. Something close to that I would be very happy with.
Should not have
• should not have my face on the cover.

```html
<!DOCTYPE html>
<html lang="en">
<head>
<meta charset="utf-8">
<title>Tobin Vesky Photography – Page Cover</title>
<link href="https://fonts.googleapis.com/css2?family=Arimo:wght@400;700&family=Montserrat:wght@300;500&display=swap" rel="stylesheet">
<style>
  :root {
    --net-blue: #4267b2;
    --link-blue: #385898;
    --page-grey: #e9ebee;
    --card-white: #ffffff;
    --line-grey: #dddfe2;
    --text-dark: #1d2129;
    --text-mid: #4b4f56;
    --text-soft: #90949c;
    --btn-grey: #f5f6f7;
    --green: #42b72a;
    --cover-bg: #26272b;
    --cover-deep: #1c1d20;
    --metal-light: #9a9b9e;
    --metal-mid: #55565a;
    --avatar-tone: #8a9aa3;
    --white: #ffffff;
  }
  * { margin: 0; padding: 0; box-sizing: border-box; }
  html, body { width: 1028px; height: 1200px; overflow: hidden; background: var(--white); }
  body { font-family: "Arimo", Arial, sans-serif; color: var(--text-dark); }
  .canvas { position: relative; width: 1028px; height: 1200px; }
  .abs { position: absolute; }

  /* browser strip */
  .address-bar { left: 0; top: 0; width: 1028px; height: 33px; background: #f7f7f7; }
  .address-text { left: 0; top: 9px; font-size: 13px; color: #555; white-space: nowrap; }

  /* network header */
  .top-nav { left: 0; top: 36px; width: 1028px; height: 40px; background: var(--net-blue); }
  .nav-mark { left: 29px; top: 44px; width: 23px; height: 23px; background: var(--white); border-radius: 2px; }
  .search-box { left: 58px; top: 44px; width: 427px; height: 23px; background: var(--white); border-radius: 2px; }
  .search-text { left: 8px; top: 4px; font-size: 13px; color: var(--text-dark); }
  .search-btn { right: 0; top: 0; width: 44px; height: 23px; background: var(--btn-grey); border-radius: 0 2px 2px 0; }
  .nav-link { top: 49px; font-size: 12.5px; font-weight: 700; color: var(--white); }

  /* page body */
  .page { left: 0; top: 76px; width: 1028px; height: 697px; background: var(--page-grey); overflow: hidden; }
  .profile-pic { left: 30px; top: 12px; width: 172px; height: 172px; border-radius: 50%; border: 4px solid var(--white); background: radial-gradient(circle at 50% 45%, #b88f78 0 28%, #5d6770 29% 55%, var(--avatar-tone) 56%); }
  .page-name { left: 29px; top: 196px; font-size: 18.5px; line-height: 25px; color: var(--text-dark); }
  .page-handle { left: 29px; top: 249px; font-size: 13px; font-weight: 700; color: var(--text-soft); }
  .side-nav { left: 24px; top: 280px; width: 177px; }
  .side-item { height: 30.7px; line-height: 27px; padding-left: 9px; font-size: 13px; color: var(--text-mid); }
  .side-item.is-active { background: #f6f7f9; border: 1px solid var(--line-grey); border-radius: 2px; font-weight: 700; color: var(--text-dark); }
  .create-btn { left: 29px; top: 475px; width: 93px; height: 23px; background: var(--green); color: var(--white); font-size: 11.5px; font-weight: 700; text-align: center; line-height: 23px; border-radius: 2px; }

  .action-bar { left: 212px; top: 299px; width: 784px; height: 49px; background: var(--card-white); border-bottom: 1px solid var(--line-grey); }
  .btn-group { left: 12px; top: 11px; height: 26px; display: flex; border: 1px solid #ced0d4; border-radius: 2px; background: var(--btn-grey); }
  .btn-group span { display: flex; align-items: center; gap: 4px; padding: 0 9px; font-size: 11.5px; font-weight: 700; color: var(--text-mid); border-right: 1px solid #ced0d4; }
  .btn-group span:last-child { border-right: 0; }
  .contact-btn { left: 497px; top: 11px; width: 135px; height: 26px; background: var(--net-blue); color: var(--white); font-size: 13px; text-align: center; line-height: 26px; border-radius: 2px; }
  .message-btn { left: 644px; top: 11px; width: 128px; height: 26px; background: var(--btn-grey); border: 1px solid #ced0d4; border-radius: 2px; font-size: 13px; color: var(--text-mid); display: flex; align-items: center; justify-content: center; gap: 5px; }

  .card { background: var(--card-white); border: 1px solid var(--line-grey); border-radius: 3px; }
  .composer { left: 212px; top: 361px; width: 478px; height: 115px; }
  .avatar { border-radius: 50%; background: radial-gradient(circle at 50% 40%, #a07a62 0 30%, #4c5258 31%); }
  .composer-hint { left: 61px; top: 23px; font-size: 13px; color: var(--text-soft); }
  .composer-rule { left: 11px; top: 67px; width: 454px; height: 1px; background: var(--line-grey); }
  .pill { top: 76px; height: 30px; background: var(--btn-grey); border-radius: 15px; font-size: 11.5px; font-weight: 700; color: var(--text-mid); display: flex; align-items: center; gap: 6px; padding-left: 9px; }

  .posts { left: 212px; top: 487px; width: 478px; height: 230px; }
  .posts-title { left: 11px; top: 11px; font-size: 13px; font-weight: 700; }
  .post { left: 11px; top: 37px; width: 455px; height: 200px; }
  .post-author { left: 56px; top: 13px; font-size: 13.5px; font-weight: 700; color: var(--link-blue); }
  .post-time { left: 56px; top: 33px; font-size: 11.5px; color: var(--text-soft); display: flex; align-items: center; gap: 3px; }
  .post-body { left: 12px; top: 57px; font-size: 13.2px; line-height: 18.1px; color: var(--text-dark); white-space: nowrap; }

  .rating { left: 702px; top: 361px; width: 294px; height: 54px; }
  .rating-badge { left: 13px; top: 13px; width: 27px; height: 27px; border-radius: 50%; background: var(--net-blue); color: var(--white); font-size: 11.5px; text-align: center; line-height: 27px; }
  .rating-text { left: 48px; top: 11px; font-size: 11.5px; line-height: 15.5px; color: var(--text-mid); }
  .rating-text b { color: var(--text-dark); }

  .ask { left: 702px; top: 428px; width: 294px; height: 188px; }
  .ask-title { left: 11px; top: 13px; font-size: 13.5px; font-weight: 700; color: var(--text-mid); }
  .ask-q { left: 11px; font-size: 11.5px; line-height: 15.5px; color: var(--text-dark); width: 190px; }
  .ask-btn { left: 229px; width: 53px; height: 22px; background: var(--btn-grey); border: 1px solid #ced0d4; border-radius: 2px; font-size: 11.5px; font-weight: 700; color: var(--text-mid); display: flex; align-items: center; justify-content: center; gap: 3px; }
  .dot { width: 11px; height: 11px; border-radius: 50%; background: var(--text-mid); display: inline-block; }
  .ask-input { left: 11px; top: 146px; width: 271px; height: 30px; border: 1px solid var(--line-grey); }
  .ask-input span { position: absolute; left: 8px; top: 8px; font-size: 11.5px; color: var(--text-soft); }
  .ask-send { right: 0; top: 0; width: 37px; height: 28px; background: var(--btn-grey); border-left: 1px solid var(--line-grey); display: flex; align-items: center; justify-content: center; }

  .community { left: 702px; top: 629px; width: 294px; height: 90px; }
  .community-title { left: 11px; top: 11px; font-size: 13.5px; font-weight: 700; }
  .see-all { right: 11px; top: 13px; font-size: 11.5px; color: var(--link-blue); }
  .invite { left: 11px; top: 43px; font-size: 11.5px; color: var(--text-mid); display: flex; align-items: center; gap: 8px; }
  .invite b { color: var(--link-blue); }

  /* staged area */
  .stage { left: 0; top: 788px; width: 1028px; height: 412px; background: linear-gradient(90deg, #b3b3b3 0%, #d7d7d7 45%, #f2f2f2 100%); }

  /* cover design */
  .cover { overflow: hidden; background: radial-gradient(ellipse at 30% 45%, var(--cover-bg) 0%, var(--cover-deep) 100%); }
  .cover.is-live { left: 212px; top: 76px; width: 784px; height: 299px; }
  .cover.is-staged { left: 130px; top: 851px; width: 775px; height: 287px; box-shadow: 0 14px 26px rgba(0,0,0,0.35); }
  .cover-photo { position: absolute; left: 44%; top: 0; width: 56%; height: 100%;
    background:
      radial-gradient(ellipse 40% 55% at 78% 80%, rgba(150,151,154,0.75) 0%, rgba(85,86,90,0.45) 50%, transparent 100%),
      radial-gradient(ellipse 45% 50% at 45% 60%, rgba(58,59,63,0.9) 0%, transparent 100%),
      radial-gradient(ellipse 22% 30% at 62% 16%, rgba(120,122,128,0.45) 0%, transparent 100%); }
  .cover-title { position: absolute; left: 69px; top: 98px; color: var(--white); font-family: "Montserrat", sans-serif; }
  .cover-name { font-weight: 500; font-size: 50px; line-height: 1; white-space: nowrap; }
  .cover-tagline { margin-top: 5px; font-weight: 300; font-size: 26px; line-height: 1; letter-spacing: 15.6px; white-space: nowrap; }
</style>
</head>
<body>
<main class="canvas">
  <div class="abs address-bar"></div>
  <div class="abs address-text">pageboard.com/tobinveskyphotography/</div>

  <header class="abs top-nav"></header>
  <div class="abs nav-mark"></div>
  <div class="abs search-box">
    <span class="abs search-text">Tobin Vesky Photography</span>
    <span class="abs search-btn">
      <svg width="44" height="23" viewBox="0 0 44 23"><circle cx="21" cy="10" r="5" fill="none" stroke="#4b4f56" stroke-width="1.6"/><line x1="25" y1="14" x2="28" y2="17" stroke="#4b4f56" stroke-width="1.8"/></svg>
    </span>
  </div>
  <span class="abs nav-link" style="left:710px">Home</span>
  <span class="abs nav-link" style="left:765px">Create</span>
  <svg class="abs" style="left:822px;top:44px" width="180" height="24" viewBox="0 0 180 24" fill="#1d2f55">
    <circle cx="9" cy="8" r="4"/><path d="M2 20c0-5 3-7 7-7s7 2 7 7z"/><circle cx="17" cy="9" r="3"/><path d="M14 20c1-4 2-6 5-6s5 2 5 6z"/>
    <circle cx="46" cy="12" r="10"/>
    <path d="M81 4c-4 0-6 3-6 7v5l-2 3h16l-2-3v-5c0-4-2-7-6-7z"/><circle cx="81" cy="21" r="2"/>
    <circle cx="123" cy="12" r="10"/><text x="123" y="17" font-size="14" font-weight="700" text-anchor="middle" fill="#4267b2" font-family="Arimo, sans-serif">?</text>
    <path d="M152 9h10l-5 6z"/>
  </svg>

  <section class="abs page">
    <div class="abs profile-pic" role="img" aria-label="Portrait photograph of the photographer"></div>
    <h1 class="abs page-name" style="font-weight:400">Tobin Vesky<br>Photography</h1>
    <div class="abs page-handle">@tobinveskyphotography</div>
    <nav class="abs side-nav">
      <div class="side-item is-active">Home</div>
      <div class="side-item">Posts</div>
      <div class="side-item">Reviews</div>
      <div class="side-item">Photos</div>
      <div class="side-item">About</div>
      <div class="side-item">Community</div>
    </nav>
    <div class="abs create-btn">Create a Page</div>

    <div class="abs action-bar">
      <div class="abs btn-group">
        <span><svg width="11" height="11" viewBox="0 0 11 11" fill="#4b4f56"><rect x="0" y="4" width="2.5" height="7"/><path d="M3.5 4l3-4c1 0 1.5 1 1 2.5L7 4h3.5l-1 7H3.5z"/></svg>Like</span>
        <span><svg width="11" height="11" viewBox="0 0 11 11" fill="none" stroke="#4b4f56" stroke-width="1.4"><circle cx="1.5" cy="9.5" r="1" fill="#4b4f56"/><path d="M1 5a5 5 0 0 1 5 5M1 1a9 9 0 0 1 9 9"/></svg>Follow</span>
        <span><svg width="12" height="11" viewBox="0 0 12 11" fill="#4b4f56"><path d="M7 0l5 5-5 5V7C4 7 2 8 0 11c0-5 3-7 7-7z"/></svg>Share</span>
        <span>•••</span>
      </div>
      <div class="abs contact-btn">Contact Us</div>
      <div class="abs message-btn"><span class="dot"></span>Send Message</div>
    </div>

    <div class="abs card composer">
      <div class="abs avatar" style="left:11px;top:11px;width:38px;height:38px" role="img" aria-label="Visitor profile photo"></div>
      <div class="abs composer-hint">Write a post...</div>
      <svg class="abs" style="left:454px;top:45px" width="16" height="16" viewBox="0 0 16 16" fill="none" stroke="#90949c" stroke-width="1.3"><circle cx="8" cy="8" r="7"/><path d="M4.5 9.5c1.5 2 5.5 2 7 0"/><circle cx="5.5" cy="6" r=".8" fill="#90949c"/><circle cx="10.5" cy="6" r=".8" fill="#90949c"/></svg>
      <div class="abs composer-rule"></div>
      <div class="abs pill" style="left:11px;width:114px"><svg width="18" height="16" viewBox="0 0 18 16"><rect x="1" y="1" width="16" height="14" rx="2" fill="#c7dbf0" stroke="#4a90d9"/><path d="M2 14l5-6 4 4 2-2 4 4z" fill="#5fb846"/></svg>Photo/Video</div>
      <div class="abs pill" style="left:132px;width:109px"><svg width="18" height="16" viewBox="0 0 18 16" fill="#4a90d9"><circle cx="8" cy="5" r="4"/><path d="M1 16c0-5 3-7 7-7s7 2 7 7z"/></svg>Tag friends</div>
      <div class="abs pill" style="left:247px;width:95px"><svg width="14" height="18" viewBox="0 0 14 18"><path d="M7 1a6 6 0 0 1 6 6c0 4-6 10-6 10S1 11 1 7a6 6 0 0 1 6-6z" fill="#f35369"/><circle cx="7" cy="7" r="2.3" fill="#fff"/></svg>Check in</div>
      <div class="abs pill" style="left:349px;width:41px;color:#90949c">•••</div>
    </div>

    <div class="abs card posts">
      <h2 class="abs posts-title">Posts</h2>
      <article class="abs card post">
        <div class="abs avatar" style="left:11px;top:11px;width:38px;height:38px" role="img" aria-label="Page profile photo"></div>
        <div class="abs post-author">Tobin Vesky Photography</div>
        <div class="abs post-time">Yesterday at 06:16 · <svg width="12" height="12" viewBox="0 0 12 12"><circle cx="6" cy="6" r="5.5" fill="#90949c"/></svg></div>
        <div class="abs" style="right:11px;top:8px;font-size:12px;color:#4b4f56">•••</div>
        <p class="abs post-body">Stepping out of the darkness and into the light. Here is Reid Calloway. All<br>the way from Saskatchewan, looking to build on his career in theater.<br>Came to me for some portfolio help. Undecided as to where to shoot,<br>figured let’s meet at the mall and sort it out from there. Then out of<br>laziness figured parking lot can make a great studio too. 😀 So here we<br>were in Larkspur Mall parking lot doing some headshot photos. Can see</p>
      </article>
    </div>

    <div class="abs card rating">
      <div class="abs rating-badge">5.0</div>
      <div class="abs rating-text"><b>5 out of 5</b> · Based on the opinion of 14<br>people</div>
    </div>

    <div class="abs card ask">
      <h2 class="abs ask-title">Ask Tobin Vesky Photography</h2>
      <div class="abs ask-q" style="top:47px">"Where are you located?"</div>
      <div class="abs ask-btn" style="top:44px"><span class="dot"></span>Ask</div>
      <div class="abs ask-q" style="top:77px">"What are your hours?"</div>
      <div class="abs ask-btn" style="top:74px"><span class="dot"></span>Ask</div>
      <div class="abs ask-q" style="top:104px">"Can you tell me more about your business?"</div>
      <div class="abs ask-btn" style="top:109px"><span class="dot"></span>Ask</div>
      <div class="abs ask-input"><span>Type a question...</span>
        <div class="abs ask-send"><svg width="14" height="12" viewBox="0 0 14 12" fill="#bec3c9"><path d="M0 0l14 6-14 6 2-6z"/></svg></div>
      </div>
    </div>

    <div class="abs card community">
      <h2 class="abs community-title">Community</h2>
      <div class="abs see-all">See all</div>
      <div class="abs invite"><svg width="14" height="12" viewBox="0 0 14 12" fill="#90949c"><circle cx="5" cy="3" r="2.5"/><path d="M0 12c0-4 2-5 5-5s5 1 5 5z"/><circle cx="10" cy="3.5" r="2"/><path d="M9 7c3 0 5 1 5 5h-3z"/></svg><span><b>Invite your friends</b> to like this Page</span></div>
    </div>
  </section>

  <section class="abs cover is-live">
    <div class="cover-photo" role="img" aria-label="Photograph of a silver film camera and a detached lens on a dark surface"></div>
    <div class="cover-title">
      <div class="cover-name">TOBIN VESKY</div>
      <div class="cover-tagline">PHOTOGRAPHY</div>
    </div>
  </section>

  <div class="abs stage"></div>
  <section class="abs cover is-staged">
    <div class="cover-photo" role="img" aria-label="Photograph of a silver film camera and a detached lens on a dark surface"></div>
    <div class="cover-title">
      <div class="cover-name">TOBIN VESKY</div>
      <div class="cover-tagline">PHOTOGRAPHY</div>
    </div>
  </section>
</main>
</body>
</html>
```